Design WORDPRESS Website for E Commerce Business

We are needing a WORDPRESS website for an E Commerce Business that is supplying quailty kids / baby products.

Target Market(s)

Female / Working Mums / New Mums

Industry/Entity Type

Business

Number of Pages Required

1 page

Font styles to use
Sans Serif

Colors
33b8a4
f8fcfd
d3a5cc
f7f1f7
cbcbcb
9d9d9d

```html
<!DOCTYPE html>
<html lang="en">
<head>
<meta charset="utf-8">
<title>Tumble &amp; Tot — Kids &amp; Baby Store</title>
<link href="https://fonts.googleapis.com/css2?family=Andika:wght@400;700&family=Fira+Sans:wght@400;500&family=Open+Sans:wght@400;600;700&family=Nunito:wght@600;700;800&display=swap" rel="stylesheet">
<style>
:root{
  --teal:#5ec7b6;
  --teal-deep:#33b8a4;
  --paper:#f8fcfd;
  --mauve:#d3a5cc;
  --blush:#f7f1f7;
  --line:#cbcbcb;
  --mute:#9d9d9d;
  --ink:#2b2b2b;
  --grey-ink:#555;
  --pink:#f48fb1;
  --rose:#e5406a;
  --orange:#f07d1e;
  --sky:#2eaee3;
  --lime:#8cd13c;
  --hot:#f0474f;
  --footer:#595959;
}
*{box-sizing:border-box;margin:0;padding:0}
html,body{width:1200px;height:2528px;overflow:hidden;background:#fff}
body{position:relative;font-family:"Open Sans",Arial,sans-serif;color:var(--ink)}
.abs{position:absolute}

/* top bar */
.topbar{left:0;top:0;width:1200px;height:38px;background:var(--teal);color:#fff;font-size:12px}
.topbar .ship{left:91px;top:11px;letter-spacing:.2px}
.topbar .currency{left:794px;top:11px}
.select{top:7px;height:24px;border:1px solid rgba(255,255,255,.6);background:rgba(255,255,255,.18);font-size:11px;padding:4px 8px;color:#fff}
.select.cur{left:860px;width:100px}
.select.lang{left:982px;width:120px}
.select::after{content:"";position:absolute;right:8px;top:9px;border:4px solid transparent;border-top-color:#fff}

/* header */
.brand{left:93px;top:76px;display:flex;align-items:center;gap:12px}
.brand .dot{width:58px;height:58px;border-radius:50%;background:var(--mute)}
.brand .name{font-family:"Nunito",sans-serif;font-weight:800;font-size:36px;line-height:36px;color:var(--teal);width:140px}
.call{left:445px;top:68px;font-size:16px;font-weight:600;display:flex;align-items:center;gap:10px}
.call .num{font-weight:400;font-size:19px;color:#333}
.search{left:445px;top:104px;width:428px;height:34px;border:1px solid #999;font-size:12px;color:var(--mute);padding:9px 12px}
.search .go{position:absolute;right:-1px;top:-1px;width:38px;height:34px;background:var(--orange)}
.account{left:955px;top:64px;font-size:14px;color:#555}
.cart{left:1020px;top:103px}
.cart .count{position:absolute;left:32px;top:-4px;width:40px;height:40px;border-radius:50%;background:var(--sky);color:#fff;font-size:17px;text-align:center;line-height:40px}

/* hero */
.hero{left:0;top:175px;width:1200px;height:452px}
.hero-art{position:absolute;inset:0;background:linear-gradient(90deg,#eef1f3 0%,#f1f3f5 38%,#e5e8ea 60%,#f4f5f6 100%)}
.hero-art .kids{position:absolute;left:560px;top:22px;width:290px;height:430px;background:linear-gradient(180deg,#e9ded6 0%,#3bb7b0 55%,#3f5c8a 100%);border-radius:40px 40px 0 0;opacity:.55}
.hero-art .crafts{position:absolute;left:880px;top:40px;width:280px;height:300px;background:radial-gradient(circle at 40% 40%,#f4b04a 0,#6fcbe4 45%,transparent 70%);opacity:.45}
.hero h1{position:absolute;left:84px;top:148px;font-family:"Andika",sans-serif;font-weight:400;font-size:50px;color:#3b3b3b}
.hero p{position:absolute;left:91px;top:222px;width:450px;font-size:12px;line-height:21px;color:#555}
.btn-more{position:absolute;left:88px;top:314px;width:190px;height:47px;border-radius:24px;background:var(--teal);color:#fff;font-size:17px;text-align:center;line-height:47px}

/* promo grid */
.promo{overflow:hidden}
.promo-winter{left:99px;top:696px;width:491px;height:489px;background:linear-gradient(90deg,#f0f0f0 0 49%,#f4f4f4 49%)}
.promo-winter .girl{position:absolute;left:40px;top:10px;width:190px;height:470px;background:linear-gradient(180deg,#e8c3ae,#f2a9c6 55%,#4e6f8f);border-radius:80px 80px 20px 20px;opacity:.7}
.promo-winter .dress{position:absolute;left:255px;top:255px;width:220px;height:220px;background:#9ee6e6;border-radius:50% 50% 8px 8px;opacity:.85}
.promo-winter .kicker{position:absolute;left:254px;top:44px;font-family:"Nunito",sans-serif;font-weight:800;font-size:34px;color:var(--rose)}
.promo-winter .year{position:absolute;left:254px;top:84px;font-family:"Nunito",sans-serif;font-weight:800;font-size:70px;color:var(--rose)}
.promo-winter .sub{position:absolute;left:258px;top:184px;font-size:21px;color:#333}
.promo-tops{left:610px;top:696px;width:234px;height:234px;background:#d9f3dc}
.promo-shoes{left:866px;top:696px;width:236px;height:234px;background:#f5f5f5}
.promo .eyebrow{position:absolute;left:24px;top:26px;font-size:13px;color:#333}
.promo .title{position:absolute;left:24px;top:46px;font-size:21px;font-weight:700;color:#222}
.promo .buy{position:absolute;left:24px;top:88px;width:88px;height:36px;background:var(--lime);color:#333;font-size:12px;text-align:center;line-height:36px}
.promo-tops .item{position:absolute;left:110px;top:100px;width:160px;height:150px;border-radius:40%;background:#e58a73}
.promo-shoes .item{position:absolute;left:0;top:140px;width:220px;height:110px;border-radius:50% 50% 10px 10px;background:#f4b7bd}
.promo-toy{left:610px;top:952px;width:492px;height:233px;background:linear-gradient(90deg,#f2ddd9,#efe3e0 60%,#f4e8e6)}
.promo-toy .item{position:absolute;left:50px;top:20px;width:135px;height:200px;border-radius:45%;background:#f09cbd}
.promo-toy .kicker{position:absolute;left:285px;top:64px;font-family:"Andika",sans-serif;font-size:26px;font-style:italic;color:#444}
.promo-toy .deal{position:absolute;left:242px;top:98px;font-family:"Nunito",sans-serif;font-weight:800;font-size:42px;color:var(--rose)}
.promo-toy .note{position:absolute;left:268px;top:150px;font-size:12px;color:#333}

/* featured */
.eyebrow-red{left:0;top:1272px;width:1200px;text-align:center;font-size:16px;color:var(--rose)}
.section-title{left:0;top:1296px;width:1200px;text-align:center;font-family:"Fira Sans",sans-serif;font-weight:500;font-size:40px;letter-spacing:1px;color:#2f2f2f}
.card{width:316px;height:320px;overflow:hidden}
.card .photo{position:absolute;inset:0}
.badge{position:absolute;top:8px;width:28px;height:28px;border-radius:50%;color:#fff;font-size:9px;text-align:center;line-height:28px;font-weight:700}
.badge.off{left:8px;background:var(--lime)}
.badge.hot{right:8px;background:var(--hot)}
.was,.now{position:absolute;bottom:16px;height:40px;font-size:14px;line-height:40px;text-align:center}
.was{left:10px;width:52px;background:#fff;color:#888;text-decoration:line-through}
.now{right:16px;width:52px;background:#222;color:#fff}
.card-title{position:absolute;left:0;top:0;width:316px;height:30px;background:#555;color:#fff;font-size:13px;padding:6px 8px}
.card-title .stars{position:absolute;right:10px;top:5px;color:#f5c623;letter-spacing:1px}
.actions{position:absolute;left:0;bottom:0;width:316px;height:78px;display:flex}
.actions span{flex:1;display:flex;align-items:center;justify-content:center}
.nav-arrow{width:48px;height:48px;border-radius:50%;background:var(--pink);display:flex;align-items:center;justify-content:center}

/* newsletter */
.news-mark{left:128px;top:2098px;width:100px;height:126px;border-radius:50px 50px 30px 30px;background:#8d8d8d}
.news-title{left:261px;top:2102px;font-size:14px;font-weight:700}
.news-copy{left:261px;top:2124px;width:340px;font-size:11px;line-height:21px;color:#888}
.news-form{left:261px;top:2179px;width:342px;height:49px;border:1px solid #ddd;font-size:14px;color:#aaa;padding:14px 18px}
.news-form .send{position:absolute;right:6px;top:6px;width:106px;height:35px;background:var(--pink);color:#fff;font-weight:700;font-size:16px;text-align:center;line-height:35px}
.social{left:720px;top:2135px;display:flex;gap:15px}
.social span{width:58px;height:58px;border-radius:50%;box-shadow:0 2px 0 rgba(0,0,0,.2)}

/* footer */
.footer{left:0;top:2271px;width:1200px;height:257px;background:var(--footer);color:#eee}
.fcol{position:absolute;top:40px}
.fcol h4{font-family:"Nunito",sans-serif;font-weight:600;font-size:17px;margin-bottom:16px}
.fcol li{list-style:none;font-size:12px;line-height:31px;color:#ddd}
.fcol .k{margin-right:6px}
</style>
</head>
<body>

<div class="abs topbar">
  <span class="abs ship">FREE SHIPPING OVER $200 FOR SELECTED COUNTIRES +DETAILS</span>
  <span class="abs currency">Currency</span>
  <span class="abs select cur">£ GBP</span>
  <span class="abs select lang">Select Language</span>
</div>

<header>
  <div class="abs brand"><span class="dot"></span><span class="name">Tumble &amp; Tot</span></div>
  <div class="abs call">Call Us Now
    <svg width="20" height="20" viewBox="0 0 24 24"><path fill="#5ec7b6" d="M6.6 10.8a15 15 0 0 0 6.6 6.6l2.2-2.2c.3-.3.7-.4 1-.2 1.1.4 2.3.6 3.6.6.6 0 1 .4 1 1V20c0 .6-.4 1-1 1A17 17 0 0 1 3 4c0-.6.4-1 1-1h3.5c.6 0 1 .4 1 1 0 1.3.2 2.5.6 3.6.1.3 0 .7-.2 1z"/></svg>
    <span class="num">+123-456-7890</span></div>
  <div class="abs search">Search
    <span class="go"><svg width="38" height="34" viewBox="0 0 38 34"><circle cx="18" cy="16" r="6" fill="none" stroke="#fff" stroke-width="2.4"/><path d="M22.5 20.5l5 5" stroke="#fff" stroke-width="2.6"/></svg></span></div>
  <div class="abs account">Sign in &nbsp;&nbsp;|&nbsp;&nbsp; Track Order</div>
  <div class="abs cart">
    <svg width="36" height="30" viewBox="0 0 36 30"><path d="M0 2h6l5 17h18l5-12H9" fill="none" stroke="#222" stroke-width="3"/><path d="M9 7h25l-5 12H11z" fill="#222"/><circle cx="13" cy="25" r="3" fill="#222"/><circle cx="27" cy="25" r="3" fill="#222"/></svg>
    <span class="count">0</span>
  </div>
</header>

<section class="abs hero">
  <div class="hero-art" role="img" aria-label="Two smiling children in summer clothes holding shopping bags in a bright playroom with paper crafts and books">
    <div class="kids"></div><div class="crafts"></div>
  </div>
  <h1>Welcome to Tumble &amp; Tot</h1>
  <p>Lorem Ipsum has been the industry's standard dummy text ever since the 1500s, when an unknown printer took a galley of type and scrambled it to make a type specimen book.</p>
  <div class="btn-more">More Details</div>
</section>

<section>
  <div class="abs promo promo-winter">
    <div class="girl" role="img" aria-label="Girl in sunglasses and a striped top with a shoulder bag"></div>
    <div class="dress" role="img" aria-label="Light aqua children's dress"></div>
    <span class="kicker">Get set</span>
    <span class="year">2017</span>
    <span class="sub">Warmm Clothes</span>
  </div>
  <div class="abs promo promo-tops">
    <div class="item" role="img" aria-label="Coral polka-dot children's top"></div>
    <span class="eyebrow">Hoods n' Tops</span>
    <span class="title">Laura's store</span>
    <span class="buy">BUY NOW</span>
  </div>
  <div class="abs promo promo-shoes">
    <div class="item" role="img" aria-label="Pink glitter children's sneakers"></div>
    <span class="eyebrow">Princess Delight</span>
    <span class="title">Shoes</span>
    <span class="buy">BUY NOW</span>
  </div>
  <div class="abs promo promo-toy">
    <div class="item" role="img" aria-label="Pink felt bunny soft toy"></div>
    <span class="kicker">toy joy</span>
    <span class="deal">30% off</span>
    <span class="note">*Limited time offer</span>
  </div>
</section>

<section>
  <div class="abs eyebrow-red">We Recommend</div>
  <h2 class="abs section-title">Featured Products</h2>

  <div class="abs card" style="left:99px;top:1378px">
    <div class="photo" role="img" aria-label="Red and yellow ride-on toy car" style="background:radial-gradient(circle at 50% 48%,#f3c432 0,#e8453a 32%,#efefef 60%)"></div>
    <div class="card-title">Simple product 07<span class="stars">★★★★★</span></div>
    <div class="actions">
      <span style="background:#45b6ea"><svg width="34" height="30" viewBox="0 0 36 30"><path d="M0 2h6l5 17h18l5-12H9" fill="none" stroke="#fff" stroke-width="3"/><circle cx="13" cy="25" r="3" fill="#fff"/><circle cx="27" cy="25" r="3" fill="#fff"/></svg></span>
      <span style="background:#f48fb1"><svg width="30" height="32" viewBox="0 0 30 32"><rect x="3" y="3" width="24" height="26" rx="3" fill="none" stroke="#fff" stroke-width="3"/><path d="M9 11h12M9 16h12M9 21h7" stroke="#fff" stroke-width="2.5"/></svg></span>
      <span style="background:#45b6ea"><svg width="34" height="30" viewBox="0 0 24 22"><path d="M12 21 2.5 11.5A5.5 5.5 0 0 1 12 4a5.5 5.5 0 0 1 9.5 7.5z" fill="#fff"/></svg></span>
      <span style="background:#f48fb1"><svg width="36" height="30" viewBox="0 0 36 30"><path d="M4 12V8h24M24 3l5 5-5 5M32 18v4H8M12 27l-5-5 5-5" fill="none" stroke="#fff" stroke-width="3.2"/></svg></span>
    </div>
  </div>
  <div class="abs card" style="left:441px;top:1378px">
    <div class="photo" role="img" aria-label="Red toy electric motorbike" style="background:radial-gradient(circle at 50% 50%,#d8222a 0,#a41920 20%,#e6e6e6 48%)"></div>
    <span class="badge off">-19%</span><span class="badge hot">HOT</span>
    <span class="was">$16</span><span class="now">$13</span>
  </div>
  <div class="abs card" style="left:782px;top:1378px">
    <div class="photo" role="img" aria-label="Baby in a black printed romper and beanie" style="background:radial-gradient(ellipse at 50% 50%,#3a3a3a 0,#555 18%,#f8c6c9 40%)"></div>
    <span class="badge off">-17%</span><span class="badge hot">HOT</span>
    <span class="was">$18</span><span class="now">$15</span>
  </div>
  <div class="abs card" style="left:99px;top:1719px">
    <div class="photo" role="img" aria-label="Purple games console with controller" style="background:radial-gradient(circle at 55% 52%,#5a4bb0 0,#4838a0 22%,#eeeeee 48%)"></div>
    <span class="badge off">-8%</span><span class="badge hot">HOT</span>
    <span class="was">$25</span><span class="now">$23</span>
  </div>
  <div class="abs card" style="left:441px;top:1719px">
    <div class="photo" role="img" aria-label="Plush bunny toy with colourful ears" style="background:radial-gradient(circle at 50% 52%,#f3e7c8 0,#e9d9b0 22%,#efeee2 50%)"></div>
    <span class="badge off">-17%</span><span class="badge hot">HOT</span>
    <span class="was">$18</span><span class="now">$15</span>
  </div>
  <div class="abs card" style="left:782px;top:1719px">
    <div class="photo" role="img" aria-label="Toddler in a cap, grey tee and black trousers" style="background:radial-gradient(ellipse at 50% 50%,#3b3b3b 0,#8a8a8a 20%,#7ecfd8 42%)"></div>
    <span class="badge hot">HOT</span>
    <span class="now" style="right:auto;left:10px">$130</span>
  </div>

  <div class="abs nav-arrow" style="left:99px;top:1676px"><svg width="16" height="20" viewBox="0 0 16 20"><path d="M12 2 4 10l8 8" fill="none" stroke="#fff" stroke-width="3"/></svg></div>
  <div class="abs nav-arrow" style="left:1050px;top:1676px"><svg width="16" height="20" viewBox="0 0 16 20"><path d="M4 2l8 8-8 8" fill="none" stroke="#fff" stroke-width="3"/></svg></div>
</section>

<section>
  <div class="abs news-mark" role="img" aria-label="Brand mark placeholder"></div>
  <div class="abs news-title">Fiora up your inbox!</div>
  <p class="abs news-copy">Claritas est etiam processus dynamicus, qui sequitur mutationem consuetudium lectorum. Your kids will thank you !</p>
  <div class="abs news-form">Email<span class="send">SEND ✉</span></div>
  <div class="abs social" aria-label="Social links">
    <span style="background:#3b66b0"></span>
    <span style="background:#2aa4e0"></span>
    <span style="background:#d6437e"></span>
    <span style="background:#e8643a"></span>
    <span style="background:#1a8ac4"></span>
    <span style="background:#e0352b"></span>
  </div>
</section>

<footer class="abs footer">
  <div class="fcol" style="left:115px"><h4>About Market</h4><ul><li>Shop</li><li>About Us</li><li>Cart</li><li>Checkout</li><li>Wishlist</li></ul></div>
  <div class="fcol" style="left:372px"><h4>Shortcode</h4><ul><li>Gallery</li><li>Accordion</li><li>Carousel</li><li>Map</li><li>Tab</li></ul></div>
  <div class="fcol" style="left:628px"><h4>My Account</h4><ul><li>My Account</li><li>My Cart</li><li>Checkout</li><li>My Wishlist</li><li>Login</li></ul></div>
  <div class="fcol" style="left:886px"><h4>Contact</h4><ul>
    <li><span class="k" style="color:#59c3f0">Email:</span>hello@tumbletot.example</li>
    <li><span class="k" style="color:#f0a030">Phone:</span>(800) 0123 4567 890</li>
    <li><span class="k" style="color:#f48fb1">Adress:</span>1234 - Bandit Tringi lAliquam</li>
    <li style="padding-left:46px">Vitae. New York</li></ul></div>
</footer>

</body>
</html>
```